Crust Harbor Hotel Coupon

Would like to design a coupon that is for hotels' staff and to be dropped off at the hotel front office anytime someone calls from a hotel and as a Thank You for hotel staff for recommending us. Coupon value to be $ 2.00. Should say Thank You or Thank you for recommending us. Need our phone number 250 614 3750 on it. Color scheme to be Green and Red as in the attached logo. Coupon to be designed for printing size 3.5 inches high and 7.5 inches wide. Rear should say Fastest Delivery, Favourite Pizza for Sports teams etc. Ask for group deals. Attached logo to be on the coupon. Coupon should say coupon # and space left for us write number

```html
<!DOCTYPE html>
<html lang="en">
<head>
<meta charset="utf-8">
<title>Crust Harbor Hotel Coupon</title>
<link rel="stylesheet" href="https://fonts.googleapis.com/css2?family=Lilita+One&family=Oswald:wght@400;500&family=Poppins:wght@600&family=Open+Sans:wght@500&display=swap">
<style>
  :root {
    --page: #2b2b2b;
    --coupon-brown: #4a2319;
    --headline-green: #2fb344;
    --value-lime: #8fd11c;
    --text-white: #ffffff;
    --stub-red: #d0343a;
    --stub-text: #3a1c14;
    --cheese: #f6b53a;
    --crust: #e9772a;
  }
  * { margin: 0; padding: 0; box-sizing: border-box; }
  html, body { width: 1200px; height: 1200px; overflow: hidden; background: var(--page); }
  .coupon {
    position: absolute; left: 40px; top: 340px;
    width: 1120px; height: 521px;
    background: var(--coupon-brown);
    color: var(--text-white);
    font-family: "Oswald", sans-serif;
  }
  .headline {
    position: absolute; left: 39px; top: 46px;
    font-family: "Lilita One", sans-serif;
    font-size: 66px; line-height: 66px;
    color: var(--headline-green);
    text-transform: uppercase; letter-spacing: -0.5px;
  }
  .value-label {
    position: absolute; left: 39px; top: 200px;
    font-size: 46px; line-height: 48px; font-weight: 400;
    text-transform: uppercase;
  }
  .value-amount {
    position: absolute; left: 336px; top: 190px;
    font-family: "Poppins", sans-serif; font-weight: 600;
    font-size: 104px; line-height: 110px;
    color: var(--value-lime); letter-spacing: -3px;
  }
  .features { position: absolute; left: 39px; top: 334px; height: 66px; width: 640px; }
  .feature { position: absolute; top: 0; display: flex; align-items: center; gap: 12px; height: 66px; }
  .feature svg { width: 52px; height: 52px; }
  .feature-text { font-size: 28px; line-height: 28px; text-transform: uppercase; }
  .feature--delivery { left: 0; }
  .feature--teams { left: 240px; }
  .feature-divider { position: absolute; left: 211px; top: 0; width: 2px; height: 72px; background: var(--text-white); }
  .order-line {
    position: absolute; left: 39px; top: 424px;
    display: flex; align-items: center; gap: 12px;
    font-family: "Lilita One", sans-serif; font-size: 52px; line-height: 60px;
    text-transform: uppercase;
  }
  .order-line svg { width: 32px; height: 32px; }
  .pizza-art {
    position: absolute; left: 652px; top: 66px; width: 437px; height: 353px;
    border-radius: 50% 50% 48% 52% / 40% 45% 55% 60%;
    background: radial-gradient(ellipse at 55% 55%, var(--cheese) 0%, var(--crust) 70%, rgba(233,119,42,0) 100%);
  }
  .brand {
    position: absolute; left: 880px; top: 56px; width: 210px;
    display: flex; align-items: center; gap: 10px;
    font-family: "Lilita One", sans-serif; font-size: 32px; line-height: 36px;
    color: var(--headline-green);
  }
  .brand-dot { width: 22px; height: 22px; border-radius: 50%; background: var(--stub-red); flex: none; }
  .coupon-number {
    position: absolute; left: 741px; top: 428px; width: 339px; height: 66px;
    background: var(--text-white);
    border: 2px dashed var(--stub-red); border-radius: 14px;
    padding-left: 22px; display: flex; align-items: center;
    font-family: "Open Sans", sans-serif; font-weight: 500; font-size: 27px;
    color: var(--stub-text);
  }
</style>
</head>
<body>
<div class="coupon">
  <h1 class="headline">Thank you for<br>recommending us</h1>
  <p class="value-label">Coupon<br>value to be</p>
  <p class="value-amount">$ 2.00</p>

  <div class="features">
    <div class="feature feature--delivery">
      <svg viewBox="0 0 52 52" fill="none" stroke="#fff" stroke-width="3" stroke-linecap="round" stroke-linejoin="round">
        <rect x="28" y="10" width="12" height="10" fill="#fff"/>
        <path d="M8 34 H42 L38 24 H24 L20 34"/>
        <path d="M14 20 L20 34"/>
        <circle cx="12" cy="38" r="5"/>
        <circle cx="40" cy="38" r="5"/>
      </svg>
      <span class="feature-text">Fastest<br>Delivery</span>
    </div>
    <div class="feature-divider"></div>
    <div class="feature feature--teams">
      <svg viewBox="0 0 52 52" fill="none" stroke="#fff" stroke-width="3" stroke-linejoin="round">
        <path d="M20 6 L46 18 L22 46 Z"/>
        <path d="M22 12 Q36 10 44 20"/>
        <circle cx="30" cy="22" r="3"/>
        <circle cx="16" cy="42" r="7" fill="#fff"/>
      </svg>
      <span class="feature-text">Favourite pizza<br>for sports teams</span>
    </div>
  </div>

  <p class="order-line">
    <span>Order now</span>
    <svg viewBox="0 0 32 32" fill="#fff"><path d="M4 12 Q16 2 28 12 L24 16 L20 12 L12 12 L8 16 Z"/><rect x="8" y="16" width="16" height="10" rx="2"/></svg>
    <span>250 614 3750</span>
  </p>

  <div class="pizza-art" role="img" aria-label="Illustration of a pepperoni pizza with a slice being lifted, melted cheese stretching, with a chili pepper and a tomato"></div>

  <div class="brand"><span class="brand-dot"></span><span>Crust Harbor</span></div>

  <div class="coupon-number">COUPON #</div>
</div>
</body>
</html>
```